Gravel Ale Label design/Graphic design

The Company
Gravel ale is an exciting new brand of ‘fit beer’ targeted at fitness enthusiasts as well as beer lovers. Gravel ale is a craft beer with added protein which can be used as a post work out recovery/leisure beverage. The target audience is generally male, 18-30 years old.
We need label/graphic design of the product to appear on our website www.gravelale-demo.co.uk

The Project
The project is to submit four designs, one for each flavour:
• Larger
• Honey Ale
• Banana Ale
• Zero Alcohol

The design of each flavour must be differentiated, yet have a consistent theme throughout all flavours. At this point Gravel ale has no official logo so feel free to incorporate this into the design, although this is not absolutely necessary.

The label/design should include the following basic information:
Brand name: Gravel Ale
Type: Larger/Honey Ale/Banana Ale/Zero
Tag: 7g High Quality Protein
Alcohol percentage: 4%/Vol (0%/Vol for the Zero alcohol version)
Volume: 300ml

Brand Guidelines (designs not necessarily limited to these)
Font: Aldrich
Main Colours: Blue # 005fbf Orange # ed7000
Basic beer bottle image attached.

The final design will be displayed on (but not limited to) the website www.gravelale-demo.co.uk

The winning designer may be contacted for future projects and opportunities with Gravel Ale.
Updates

Project Deadline Extended
Reason: My apologies I have been sick the last few days and have been unable to provide feedback. Your work is much appreciated, I will extend the project to give us a little more time and provide feedback individually later today. Best Regards, Oliver

Target Market(s)

The target audience is generally male, 18-30 years old.

Industry/Entity Type

Fitness

Requirements
Must have
• The label/design should include the following basic information:
Brand name: Gravel Ale
Volume: 300ml

```html
<!DOCTYPE html>
<html lang="en">
<head>
<meta charset="utf-8">
<title>Gravel Ale – Flavour Labels</title>
<link rel="stylesheet" href="https://fonts.googleapis.com/css2?family=Oswald:wght@500;700&family=Cinzel:wght@500&display=swap">
<style>
  :root {
    --page: #ffffff;
    --cream: #f3e2b3;
    --honey-bg: #1f1c1d;
    --honey-edge: #f29a1f;
    --honey-ink: #f29a1f;
    --banana-bg: #f4b31a;
    --banana-oval: #221e1f;
    --banana-ink: #e8c25a;
    --zero-bg: #1a9148;
    --zero-oval: #157a3b;
    --zero-edge: #0e5a2b;
    --lager-bg: #e4202b;
    --lager-oval: #b5141e;
    --lager-edge: #7a0c12;
    --white: #ffffff;
  }
  html, body {
    margin: 0;
    width: 1200px;
    height: 848px;
    overflow: hidden;
    background: var(--page);
  }
  .label-row {
    position: absolute;
    top: 311px;
    left: 20px;
    display: flex;
    gap: 40px;
  }
  .label {
    position: relative;
    width: 260px;
    height: 226px;
    background: var(--bg);
    color: var(--ink);
    font-family: "Oswald", sans-serif;
  }
  .label__tag {
    position: absolute;
    left: 6px;
    top: 8px;
    writing-mode: vertical-rl;
    font-size: 9px;
    font-weight: 500;
    letter-spacing: 0.4px;
    text-transform: uppercase;
  }
  .label__abv {
    position: absolute;
    left: 6px;
    bottom: 6px;
    line-height: 1;
    font-weight: 500;
  }
  .label__abv small { font-size: 7px; display: block; }
  .label__abv strong { font-size: 26px; font-weight: 500; }
  .label__abv span { font-size: 8px; display: block; margin-top: 2px; }
  .label__vol {
    position: absolute;
    right: 6px;
    bottom: 6px;
    text-align: right;
    line-height: 1;
    font-weight: 500;
  }
  .label__vol small { font-size: 7px; display: block; }
  .label__vol span { font-size: 14px; }
  .badge {
    position: absolute;
    left: 45px;
    top: 0;
    width: 170px;
    height: 222px;
    box-sizing: border-box;
    border-radius: 50%;
    background: var(--oval);
    border: 3px solid var(--edge);
    overflow: hidden;
    display: flex;
    flex-direction: column;
    align-items: center;
  }
  .badge__flavour {
    margin-top: 20px;
    font-family: "Cinzel", serif;
    font-size: 11px;
    letter-spacing: 2px;
    color: var(--flavour);
    text-transform: uppercase;
  }
  .badge__emblem {
    width: 110px;
    height: 34px;
    margin-top: 6px;
    border-radius: 55px 55px 0 0;
    background: radial-gradient(ellipse at 50% 100%, var(--cream), rgba(243,226,179,0.35));
  }
  .badge__name {
    margin: 2px 0 0;
    font-family: "Oswald", sans-serif;
    font-weight: 700;
    text-align: center;
    line-height: 0.9;
    color: var(--name);
  }
  .badge__name span { display: block; }
  .badge__name .top { font-size: 26px; letter-spacing: 2px; }
  .badge__name .bottom { font-size: 56px; }
  .badge__ornament {
    width: 70px;
    height: 22px;
    margin-top: 6px;
    border-radius: 11px;
    background: linear-gradient(90deg, rgba(243,226,179,0.2), var(--cream), rgba(243,226,179,0.2));
  }

  .label--honey  { --bg: var(--honey-bg);  --ink: var(--honey-ink); --oval: var(--honey-bg); --edge: var(--honey-edge); --flavour: var(--white); --name: var(--white); }
  .label--banana { --bg: var(--banana-bg); --ink: var(--banana-oval); --oval: var(--banana-oval); --edge: var(--banana-oval); --flavour: var(--banana-ink); --name: var(--banana-ink); }
  .label--zero   { --bg: var(--zero-bg);   --ink: var(--white); --oval: var(--zero-oval); --edge: var(--zero-edge); --flavour: var(--white); --name: var(--white); }
  .label--lager  { --bg: var(--lager-bg);  --ink: var(--white); --oval: var(--lager-oval); --edge: var(--lager-edge); --flavour: var(--white); --name: var(--white); }
</style>
</head>
<body>
  <main class="label-row">
    <article class="label label--honey">
      <p class="label__tag" style="margin:0">7g High Quality Protein</p>
      <div class="label__abv"><small>ALC.</small><strong>4%</strong><span>BY VOLUME</span></div>
      <div class="badge">
        <div class="badge__flavour">Honey Ale</div>
        <div class="badge__emblem" role="img" aria-label="Sunburst emblem with barbell ornament"></div>
        <h2 class="badge__name"><span class="top">GRAVEL</span><span class="bottom">ALE</span></h2>
        <div class="badge__ornament" role="img" aria-label="Laurel wreath and star ornament"></div>
      </div>
      <div class="label__vol"><small>VOL.</small><span>300ML</span></div>
    </article>

    <article class="label label--banana">
      <p class="label__tag" style="margin:0">7g High Quality Protein</p>
      <div class="label__abv"><small>ALC.</small><strong>4%</strong><span>BY VOLUME</span></div>
      <div class="badge">
        <div class="badge__flavour">Banana Ale</div>
        <div class="badge__emblem" role="img" aria-label="Sunburst emblem with barbell ornament"></div>
        <h2 class="badge__name"><span class="top">GRAVEL</span><span class="bottom">ALE</span></h2>
        <div class="badge__ornament" role="img" aria-label="Laurel wreath and star ornament"></div>
      </div>
      <div class="label__vol"><small>VOL.</small><span>300ML</span></div>
    </article>

    <article class="label label--zero">
      <p class="label__tag" style="margin:0">7g High Quality Protein</p>
      <div class="label__abv"><small>ALC.</small><strong>0%</strong><span>BY VOLUME</span></div>
      <div class="badge">
        <div class="badge__flavour">Zero</div>
        <div class="badge__emblem" role="img" aria-label="Sunburst emblem with barbell ornament"></div>
        <h2 class="badge__name"><span class="top">GRAVEL</span><span class="bottom">ALE</span></h2>
        <div class="badge__ornament" role="img" aria-label="Laurel wreath and star ornament"></div>
      </div>
      <div class="label__vol"><small>VOL.</small><span>300ML</span></div>
    </article>

    <article class="label label--lager">
      <p class="label__tag" style="margin:0">7g High Quality Protein</p>
      <div class="label__abv"><small>ALC.</small><strong>4%</strong><span>BY VOLUME</span></div>
      <div class="badge">
        <div class="badge__flavour">Larger</div>
        <div class="badge__emblem" role="img" aria-label="Sunburst emblem with barbell ornament"></div>
        <h2 class="badge__name"><span class="top">GRAVEL</span><span class="bottom">ALE</span></h2>
        <div class="badge__ornament" role="img" aria-label="Laurel wreath and star ornament"></div>
      </div>
      <div class="label__vol"><small>VOL.</small><span>300ML</span></div>
    </article>
  </main>
</body>
</html>
```